VelaMend Wellness Business Cards

I am looking to have luxury business cards made for my IV Therapy and Wellness business.

Target Market(s)

Health and Wellness professionals

Industry/Entity Type

MedSpa

Contact Information for Business Card

Tobin Hargreave, MSN, RN, CCRN Tobin@velamendwellness.com (916) 582-1937 QR code to website www.velamendwellness.com

```html
<!DOCTYPE html>
<html lang="en">
<head>
<meta charset="utf-8">
<title>VelaMend Wellness Business Cards</title>
<link rel="stylesheet" href="https://fonts.googleapis.com/css2?family=Montserrat:wght@500;800&family=Arimo:wght@400&display=swap">
<style>
  :root {
    --backdrop: #2b2b31;
    --card: #ffffff;
    --navy: #2a2566;
    --sky: #2ba3df;
    --gold: #b08a3a;
    --ink: #1e1e22;
  }
  * { margin: 0; padding: 0; box-sizing: border-box; }
  html, body { width: 1200px; height: 801px; overflow: hidden; }
  body {
    background: var(--backdrop);
    position: relative;
    font-family: "Arimo", Arial, sans-serif;
  }
  .card {
    position: absolute;
    top: 246px;
    width: 540px;
    height: 309px;
    background: var(--card);
    box-shadow: 0 18px 40px rgba(0,0,0,0.45);
    overflow: hidden;
  }
  .card--front { left: 30px; }
  .card--back { left: 630px; }

  .wordmark {
    position: absolute;
    font-family: "Montserrat", Arial, sans-serif;
    line-height: 1.1;
    white-space: nowrap;
  }
  .wordmark--navy { color: var(--navy); font-weight: 800; }
  .wordmark--gold { color: var(--gold); font-weight: 500; text-align: center; }

  .card--front .wordmark--navy { left: 60px; top: 122px; font-size: 32px; }
  .card--front .wordmark--gold { left: 330px; top: 98px; font-size: 22px; }

  .card--back .wordmark--navy { right: 44px; top: 42px; font-size: 26px; }
  .card--back .wordmark--gold { right: 44px; top: 168px; font-size: 20px; }

  .divider {
    position: absolute;
    left: 40px;
    right: 28px;
    top: 124px;
    height: 2px;
    background: var(--gold);
  }
  .holder {
    position: absolute;
    left: 40px;
    top: 64px;
  }
  .holder__name {
    font-family: "Montserrat", Arial, sans-serif;
    font-weight: 800;
    font-size: 19px;
    color: var(--navy);
    letter-spacing: 0.3px;
  }
  .holder__role {
    font-family: "Montserrat", Arial, sans-serif;
    font-weight: 500;
    font-size: 14px;
    color: var(--sky);
    margin-top: 2px;
  }
  .contact {
    position: absolute;
    left: 40px;
    top: 144px;
    font-size: 13px;
    color: var(--ink);
    line-height: 1.45;
    list-style: none;
  }
  .contact__item { display: flex; align-items: center; gap: 8px; }
  .contact__item--plain { padding-left: 20px; }
  .contact__icon { width: 12px; height: 12px; flex: none; }
</style>
</head>
<body>

<section class="card card--front" aria-label="Card front">
  <div class="wordmark wordmark--navy">VelaMend<br>Wellness</div>
  <div class="wordmark wordmark--gold">VelaMend<br>Wellness</div>
</section>

<section class="card card--back" aria-label="Card back">
  <div class="holder">
    <div class="holder__name">CORIN L. ASHBY</div>
    <div class="holder__role">President</div>
  </div>
  <div class="wordmark wordmark--navy">VelaMend<br>Wellness</div>
  <div class="divider"></div>
  <ul class="contact">
    <li class="contact__item contact__item--plain">PO Box 7812</li>
    <li class="contact__item contact__item--plain">Harbor Road, 2nd Lane</li>
    <li class="contact__item contact__item--plain">United States</li>
    <li class="contact__item">
      <svg class="contact__icon" viewBox="0 0 12 12"><rect x="2" y="1" width="8" height="10" rx="1.5" fill="none" stroke="var(--gold)" stroke-width="1.4"/></svg>
      0147 258 369
    </li>
    <li class="contact__item">
      <svg class="contact__icon" viewBox="0 0 12 12"><rect x="0.5" y="2" width="11" height="8" fill="var(--gold)"/><path d="M0.5 2 L6 7 L11.5 2" fill="none" stroke="#fff" stroke-width="1"/></svg>
      info@velamendmail.com
    </li>
    <li class="contact__item">
      <svg class="contact__icon" viewBox="0 0 12 12"><circle cx="6" cy="6" r="5.3" fill="none" stroke="var(--gold)" stroke-width="1.2"/><ellipse cx="6" cy="6" rx="2.3" ry="5.3" fill="none" stroke="var(--gold)" stroke-width="1"/><path d="M0.7 6 H11.3" stroke="var(--gold)" stroke-width="1"/></svg>
      www.velamendweb.com
    </li>
  </ul>
  <div class="wordmark wordmark--gold">VelaMend<br>Wellness</div>
</section>

</body>
</html>
```